Christmas 2024 Halcyon and Fielder

We need a greeting card (front and back) for Christmas and New Year 2025.
The design should be appropriate for the Christmas season and based on our current flyer (attached). Feel free to include graphics.
The contents of the flyer are attached as a PDF file.
The size/dimensions are attached as a PDF file!

Thank you!

Requirements
Must have
• Font Montserrat, modern design, not too much content

```html
<!DOCTYPE html>
<html lang="de">
<head>
<meta charset="utf-8">
<title>Weihnachtskarte 2024 – Halcyon and Fielder</title>
<link rel="stylesheet" href="https://fonts.googleapis.com/css2?family=Montserrat:wght@400;700&family=Great+Vibes&display=swap">
<style>
  :root {
    --backdrop: #d5d5d3;
    --card-black: #050607;
    --gold: #fec42f;
    --gold-soft: rgba(254,196,47,0.55);
    --gold-faint: rgba(254,196,47,0.08);
    --band-brown: #3d3324;
    --text-light: #f2f2f2;
    --ink: #0b0b0b;
  }
  html, body {
    margin: 0;
    width: 1200px;
    height: 1200px;
    overflow: hidden;
    background: var(--backdrop);
    font-family: "Montserrat", sans-serif;
  }
  .card {
    position: absolute;
    top: 335px;
    width: 527px;
    height: 528px;
    background: var(--card-black);
    overflow: hidden;
    box-shadow: 0 6px 14px rgba(0,0,0,0.35);
  }
  .card--front { left: 53px; }
  .card--back { left: 615px; }
  .diagonal-band {
    position: absolute;
    inset: 0;
    width: 100%;
    height: 100%;
  }
  .brand-name {
    position: absolute;
    top: 104px;
    left: 0;
    width: 100%;
    text-align: center;
    font-weight: 700;
    font-size: 30px;
    line-height: 42px;
    letter-spacing: 0.5px;
    color: var(--gold);
  }
  .illustration {
    position: absolute;
  }
  .illustration--tree-scene {
    left: 136px;
    top: 239px;
    width: 254px;
    height: 183px;
    background:
      radial-gradient(ellipse 22% 90% at 50% 100%, var(--gold-soft), transparent 100%),
      radial-gradient(ellipse 12% 28% at 13% 100%, var(--gold-soft), transparent 100%),
      radial-gradient(ellipse 12% 34% at 88% 100%, var(--gold-soft), transparent 100%),
      linear-gradient(180deg, transparent, var(--gold-faint));
  }
  .greeting-bar {
    position: absolute;
    left: 0;
    top: 422px;
    width: 100%;
    height: 106px;
    background: var(--gold);
    display: flex;
    align-items: center;
    justify-content: center;
    text-align: center;
    font-weight: 700;
    font-size: 21px;
    line-height: 29px;
    color: var(--ink);
  }
  .greeting-bar p { margin: 0; }
  .illustration--ornaments-left,
  .illustration--ornaments-right {
    top: 0;
    width: 78px;
    height: 150px;
    background:
      radial-gradient(circle 20px at 50% 87%, var(--gold-soft), transparent 100%),
      linear-gradient(180deg, var(--gold-faint), rgba(254,196,47,0.16));
  }
  .illustration--ornaments-left { left: 28px; }
  .illustration--ornaments-right { left: 423px; }
  .salutation {
    position: absolute;
    left: 137px;
    top: 108px;
    width: 253px;
    height: 29px;
    margin: 0;
    background: var(--gold);
    color: var(--ink);
    font-weight: 700;
    font-size: 16.5px;
    display: flex;
    align-items: center;
    justify-content: center;
    white-space: nowrap;
  }
  .message {
    position: absolute;
    left: 0;
    width: 100%;
    margin: 0;
    text-align: center;
    color: var(--text-light);
    font-size: 14.5px;
    line-height: 20.7px;
    white-space: nowrap;
  }
  .message--thanks { top: 188px; }
  .message--wishes { top: 268px; }
  .message--closing {
    top: 348px;
    font-size: 14px;
    font-weight: 700;
  }
  .signatures {
    position: absolute;
    left: 0;
    top: 376px;
    width: 100%;
    font-family: "Great Vibes", cursive;
    font-size: 20px;
    color: var(--gold);
  }
  .signature-row {
    display: flex;
    justify-content: center;
    gap: 40px;
    height: 29px;
    line-height: 29px;
    white-space: nowrap;
  }
  .signature-row--wide { gap: 46px; }
  .signature-row .amp { margin: 0 -26px; }
</style>
</head>
<body>

<section class="card card--front" aria-label="Kartenvorderseite">
  <svg class="diagonal-band" viewBox="0 0 527 528" aria-hidden="true">
    <defs>
      <linearGradient id="front-band-fade" x1="0" y1="0" x2="0" y2="1">
        <stop offset="0" stop-color="#3d3324" stop-opacity="1"/>
        <stop offset="0.35" stop-color="#3d3324" stop-opacity="0.85"/>
        <stop offset="0.62" stop-color="#3d3324" stop-opacity="0"/>
      </linearGradient>
    </defs>
    <polygon points="220,0 333,0 90,340 0,340 0,310" fill="url(#front-band-fade)"/>
  </svg>

  <div class="brand-name">Halcyon and Fielder</div>

  <div class="illustration illustration--tree-scene" role="img" aria-label="Goldene Linienzeichnung eines Tannenbaums mit Stern, flankiert von zwei Hirschsilhouetten"></div>

  <div class="greeting-bar">
    <p>Frohe Weihnachten und<br>ein glückliches neues Jahr 2025!</p>
  </div>
</section>

<section class="card card--back" aria-label="Kartenrückseite">
  <svg class="diagonal-band" viewBox="0 0 527 528" aria-hidden="true">
    <defs>
      <linearGradient id="back-band-fade" x1="0" y1="1" x2="0" y2="0">
        <stop offset="0" stop-color="#3d3324" stop-opacity="1"/>
        <stop offset="0.45" stop-color="#3d3324" stop-opacity="0.8"/>
        <stop offset="0.75" stop-color="#3d3324" stop-opacity="0"/>
      </linearGradient>
    </defs>
    <polygon points="194,528 306,528 527,215 527,200 450,200" fill="url(#back-band-fade)"/>
  </svg>

  <div class="illustration illustration--ornaments-left" role="img" aria-label="Hängende goldene Schneeflocken, Rauten und Christbaumkugel"></div>
  <div class="illustration illustration--ornaments-right" role="img" aria-label="Hängende goldene Schneeflocken, Rauten und Christbaumkugel"></div>

  <h1 class="salutation">Liebe Kooperationspartner,</h1>

  <p class="message message--thanks">zum Jahresende ein herzliches<br>Dankeschön für die vertrauensvolle und<br>professionelle Zusammenarbeit.</p>

  <p class="message message--wishes">Das Team von Halcyon and Fielder wünscht ein<br>frohes Weihnachtsfest, erholsame Feiertage und einen<br>erfolgreichen Start in das neue Jahr 2025!</p>

  <p class="message message--closing">In diesem Sinne viele Grüße aus Lindenau,</p>

  <div class="signatures">
    <div class="signature-row signature-row--wide"><span>Anton Berwald</span><span>Lukas Ferrand</span><span>Jonas Berwald</span></div>
    <div class="signature-row signature-row--wide"><span>Clara Berwald</span><span>Miriam Tesch</span></div>
    <div class="signature-row"><span>Sophie Lanz</span></div>
    <div class="signature-row"><span>Tobias Wendel</span><span class="amp">&amp;</span><span>Henrik Noll</span></div>
  </div>
</section>

</body>
</html>
```